Business Card & Stationary for Orthodontic Office
Lena Voss Orthodontics
Business Card & Stationary for Orthodontic Office  - Medical
Creative Brief
Professional
See Additional Comments
4127 Marlow Ct Westbrook, NY 14398
Info@SmileCraftClinics.com
www.SmileCraftClinics.com
The logo contains our DBA name however below should read smaller; Lena Voss D.M.D. M.S. PC Also the NCT attached should be included as well.
(additional locations) Brenford 5193 Hollin Ridge Ave. Brenford, NY 14387 (716)555-0193 Corvell Falls 2615 Fenwick Rd. Corvell Falls, NY 14391 (716)555-0147 Harlow 58 Lorimer St. Harlow, NY 14802 (585)555-0126 Ashmere 4712 W. Tarrow St. Ashmere, NY 14906 (585)555-0126
LVBrace LVBrace
*************EDIT TO BRIEF*************** We are no longer requiring the NCT logo instead under Lena Voss D.M.D. M.S. PC it should say; "Board Certified Orthodontist" Obviously this is without the quotations. Also the back side of the business card MUST include the remaining office locations. If your draft is submitted without this information on the back it WILL BE ELIMINATED!
*****PLEASE READ THE BRIEF BEFORE SUBMITTING DESIGNS AS THE NCT LOGO MUST BE INCLUDED******** We need all new office supplies as one of our doctors has retired. Business cards (front and back) Stationary (letterhead, envelopes #10, large flat envelopes 12"x15") Included in the brief is a copy of our current letterhead and business card (front & back) to be used as a base point. Our remaining doctor is young, professional, and very modern. Please let this be reflected in the designs that you present.

```html
<!DOCTYPE html>
<html lang="en">
<head>
<meta charset="utf-8">
<title>Lena Voss Orthodontics – Business Card</title>
<link rel="stylesheet" href="https://fonts.googleapis.com/css2?family=Cinzel:wght@400;600&family=Raleway:wght@500&display=swap">
<style>
  :root {
    --backdrop: #e4e5e7;
    --card-white: #ffffff;
    --brand-green: #7fcb1c;
    --brand-blue: #1f6fb5;
    --brand-teal: #2a8fc0;
    --ink-dark: #3a4a55;
    --ink-green: #5aa312;
    --faint-blue: #cfe3f1;
    --faint-green: #dcefc4;
  }
  * { margin: 0; padding: 0; box-sizing: border-box; }
  html, body { width: 1200px; height: 895px; overflow: hidden; }
  body { background: var(--backdrop); position: relative; font-family: "Cinzel", serif; }

  .card {
    position: absolute;
    width: 540px;
    height: 309px;
    background: var(--card-white);
    overflow: hidden;
    box-shadow: 0 2px 6px rgba(0,0,0,0.12);
  }
  .card--back { left: 600px; top: 110px; }
  .card--front { left: 60px; top: 476px; }

  /* Back card */
  .faint-mark {
    position: absolute;
    right: 22px; top: 70px;
    width: 190px; height: 190px;
    border-radius: 50%;
    background: linear-gradient(135deg, var(--faint-green), var(--faint-blue));
    display: flex; align-items: center; justify-content: center;
  }
  .faint-mark__name { font-size: 30px; font-weight: 400; color: #ffffff; letter-spacing: 1px; }

  .locations {
    position: absolute;
    left: 30px; top: 44px;
    display: grid;
    grid-template-columns: 140px 150px;
    column-gap: 12px; row-gap: 30px;
  }
  .location { display: flex; gap: 7px; }
  .location__pin { flex: none; width: 11px; height: 15px; margin-top: 1px; }
  .location__city { font-size: 11px; font-weight: 600; color: var(--ink-green); letter-spacing: 0.5px; }
  .location__line { font-size: 9.5px; color: var(--ink-dark); line-height: 1.35; white-space: nowrap; }

  /* Front card */
  .front-art { position: absolute; inset: 0; }
  .brand {
    position: absolute;
    left: 62px; top: 40px;
    display: flex; align-items: center; gap: 12px;
  }
  .brand__dot { width: 50px; height: 50px; border-radius: 50%; background: var(--brand-green); }
  .brand__name { font-size: 25px; font-weight: 400; color: var(--brand-teal); letter-spacing: 1px; line-height: 1; }

  .details {
    position: absolute;
    left: 44px; top: 208px;
    color: #ffffff;
    font-size: 10.5px;
    line-height: 1.45;
    letter-spacing: 0.3px;
  }
  .details__doctor { margin-bottom: 14px; }

  .contacts {
    position: absolute;
    left: 300px; top: 196px;
    list-style: none;
    color: #ffffff;
    font-family: "Raleway", sans-serif;
    font-size: 9.5px;
    line-height: 1;
  }
  .contacts li { display: flex; align-items: center; gap: 6px; height: 15px; }
  .contacts__icon {
    width: 10px; height: 10px; border-radius: 50%;
    border: 1px solid #ffffff;
    flex: none;
  }
</style>
</head>
<body>

<section class="card card--back" aria-label="Business card back – office locations">
  <div class="faint-mark"><span class="faint-mark__name">LVBrace</span></div>

  <div class="locations">
    <div class="location">
      <svg class="location__pin" viewBox="0 0 11 15"><path d="M5.5 0A5.5 5.5 0 0 0 0 5.5C0 9.5 5.5 15 5.5 15S11 9.5 11 5.5A5.5 5.5 0 0 0 5.5 0Zm0 7.6a2.1 2.1 0 1 1 0-4.2 2.1 2.1 0 0 1 0 4.2Z" fill="#7fcb1c"/></svg>
      <div>
        <p class="location__city">Harlow</p>
        <p class="location__line">58 Lorimer St.</p>
        <p class="location__line">Harlow, NY 14802</p>
        <p class="location__line">(585)555-0126</p>
      </div>
    </div>
    <div class="location">
      <svg class="location__pin" viewBox="0 0 11 15"><path d="M5.5 0A5.5 5.5 0 0 0 0 5.5C0 9.5 5.5 15 5.5 15S11 9.5 11 5.5A5.5 5.5 0 0 0 5.5 0Zm0 7.6a2.1 2.1 0 1 1 0-4.2 2.1 2.1 0 0 1 0 4.2Z" fill="#7fcb1c"/></svg>
      <div>
        <p class="location__city">Brenford</p>
        <p class="location__line">5193 Hollin Ridge Ave.</p>
        <p class="location__line">Brenford, NY 14387</p>
        <p class="location__line">(716)555-0193</p>
      </div>
    </div>
    <div class="location">
      <svg class="location__pin" viewBox="0 0 11 15"><path d="M5.5 0A5.5 5.5 0 0 0 0 5.5C0 9.5 5.5 15 5.5 15S11 9.5 11 5.5A5.5 5.5 0 0 0 5.5 0Zm0 7.6a2.1 2.1 0 1 1 0-4.2 2.1 2.1 0 0 1 0 4.2Z" fill="#7fcb1c"/></svg>
      <div>
        <p class="location__city">Ashmere</p>
        <p class="location__line">4712 W. Tarrow St.</p>
        <p class="location__line">Ashmere, NY 14906</p>
        <p class="location__line">(585)555-0126</p>
      </div>
    </div>
    <div class="location">
      <svg class="location__pin" viewBox="0 0 11 15"><path d="M5.5 0A5.5 5.5 0 0 0 0 5.5C0 9.5 5.5 15 5.5 15S11 9.5 11 5.5A5.5 5.5 0 0 0 5.5 0Zm0 7.6a2.1 2.1 0 1 1 0-4.2 2.1 2.1 0 0 1 0 4.2Z" fill="#7fcb1c"/></svg>
      <div>
        <p class="location__city">Corvell Falls</p>
        <p class="location__line">2615 Fenwick Rd.</p>
        <p class="location__line">Corvell, NY 14391</p>
        <p class="location__line">(716)555-0147</p>
      </div>
    </div>
  </div>
</section>

<section class="card card--front" aria-label="Business card front">
  <svg class="front-art" viewBox="0 0 540 309" preserveAspectRatio="none" aria-hidden="true">
    <defs>
      <linearGradient id="greenField" x1="0" y1="0" x2="0" y2="1">
        <stop offset="0" stop-color="#a6e02e"/>
        <stop offset="1" stop-color="#6fbf16"/>
      </linearGradient>
    </defs>
    <path d="M0 128 C140 150 300 170 540 122 L540 150 C320 196 150 180 0 152 Z" fill="#1f6fb5"/>
    <path d="M0 140 C150 164 320 180 540 136 L540 150 C320 196 150 180 0 152 Z" fill="#2a8fc0"/>
    <path d="M0 156 C150 186 330 200 540 158 L540 309 L0 309 Z" fill="url(#greenField)"/>
  </svg>

  <div class="brand">
    <span class="brand__dot"></span>
    <span class="brand__name">Lena Voss Orthodontics</span>
  </div>

  <div class="details">
    <p class="details__doctor">Lena Voss D.M.D. M.S. PC</p>
    <p>4127 Marlow Ct</p>
    <p>Westbrook, NY 14398</p>
  </div>

  <ul class="contacts">
    <li><span class="contacts__icon"></span>(716)555-0172</li>
    <li><span class="contacts__icon"></span>(716)555-0188</li>
    <li><span class="contacts__icon"></span>Info@SmileCraftClinics.com</li>
    <li><span class="contacts__icon"></span>www.SmileCraftClinics.com</li>
  </ul>
</section>

</body>
</html>
```